International freight forwarder experienced in perishable handling needs a web design

We need a website designed that will allow us to capture more customers through the website. We would like a visually appealing design that is not so heavy on text. Our business covers the logistics and freight forwarding industries and we have offices in South America and the USA. Our main customers are importers USA, Europe, Asia and Russia and we currently work almost exclusively with perishable products such as fresh cut flowers, fresh exotics fruits, cacao, fresh fish etc. We would like to convey a fresh, modern approach to freight forwarding focusing on concepts such as - time sensitive, anytime-anywhere delivery, innovation, experience, reliability and confidence. Should include links with Chatterpost and Workvine. Our core solutions include: Core Services
*Air Freight
*Ocean Freight
*Warehousing & Distribution
Our industry solutions cover
*Flowers
*FMCG including, fruits, vegetables
*Live animals
*Automotive
*Consumer Goods
*Industrial
*Oil & Gas
*Pharma
* Event logistics
* Project logistics

Target Market(s)

Importers in Europe, USA, Asia, Middle East and Russia

Number of Pages Required

4 page

Font styles to use
Sans Serif

Colors
a1cd39
606060
000000

Requirements
Must have
• Photos of fresh cut flowers, FMCG such as cacao, fresh fish (packaged for shipping), fresh exotic fruits, pharma products (packaged for shipping), oil and gas etc. Internal customer login access
Nice to have
• Photos of cargo shipping carriers and cargo airline carriers. Features similar to those of following website http://www.vantoshipping.example/eng/main/index.jsp?FromURL=web
Should not have
• Too much text, needs to be visually pleasing

```html
<!DOCTYPE html>
<html lang="en">
<head>
<meta charset="utf-8">
<title>Freightmere Alliance</title>
<link href="https://fonts.googleapis.com/css2?family=Open+Sans:wght@400;600;700;800&display=swap" rel="stylesheet">
<style>
:root{
  --green:#a1cd39;
  --green-deep:#6fa12a;
  --ink:#000000;
  --grey:#606060;
  --dark:#353535;
  --footer:#151515;
  --white:#ffffff;
}
*{margin:0;padding:0;box-sizing:border-box}
html,body{width:743px;height:1200px;overflow:hidden}
body{font-family:"Open Sans",sans-serif;color:var(--grey);background:var(--white);position:relative}
.abs{position:absolute}

/* header */
.site-header{position:absolute;left:0;top:0;width:743px;height:41px;background:var(--white)}
.brand{position:absolute;left:166px;top:10px;display:flex;align-items:center;gap:6px}
.brand-dot{width:20px;height:20px;border-radius:50%;background:var(--green)}
.brand-name{font-size:13px;font-weight:700;color:#3a3a3a;letter-spacing:-.2px}
.main-nav{position:absolute;left:333px;top:16px;display:flex;font-size:5.2px;font-weight:700;color:#333;text-transform:uppercase}
.main-nav span{padding:0 4px;border-left:1px solid #333;line-height:6px}
.main-nav span:first-child{border:none;padding-left:0;color:var(--green)}
.round-btn{position:absolute;top:13px;width:16px;height:16px;border:1px solid var(--green);border-radius:50%;display:flex;align-items:center;justify-content:center}

/* hero */
.hero{position:absolute;left:0;top:41px;width:743px;height:267px;background:linear-gradient(180deg,#7fa7d2 0%,#b9cfe6 45%,#b49a80 80%,#8b6b55 100%)}
.hero-kicker{position:absolute;top:33px;width:100%;text-align:center;color:var(--white);font-size:8.5px;font-weight:700}
.hero-title{position:absolute;top:45px;width:100%;text-align:center;color:var(--white);font-size:20px;font-weight:700;line-height:22px;text-shadow:0 1px 3px rgba(0,0,0,.3)}
.service-card{position:absolute;top:133px;width:130px;height:112px;background:rgba(111,161,42,.85);color:var(--white);padding:13px 15px}
.service-card h3{font-size:9px;font-weight:700;line-height:10px;margin-bottom:6px}
.service-card p{font-size:5px;line-height:7.8px}
.btn-outline{position:absolute;left:15px;bottom:12px;border:1px solid var(--white);font-size:5.6px;font-weight:700;padding:2px 7px}

/* industries */
.industries{position:absolute;left:0;top:308px;width:743px;height:320px;background:var(--dark)}
.map-fill{position:absolute;left:180px;top:150px;width:400px;height:170px;background:rgba(255,255,255,.04);border-radius:50%}
.section-title{position:absolute;width:100%;text-align:center;font-size:10.5px;font-weight:700;color:var(--white)}
.title-rule{position:absolute;left:316px;width:111px;height:6px}
.industry{position:absolute;width:100px}
.industry .head{display:flex;gap:5px;align-items:flex-start;color:var(--green);font-size:6.5px;font-weight:700;text-transform:uppercase;line-height:8px}
.industry .icon{width:13px;height:11px;flex:none}
.industry p{margin:10px 0 0 19px;color:#e4e4e4;font-size:5.2px;line-height:8px}

/* testimonials */
.testimonials{position:absolute;left:0;top:628px;width:743px;height:240px;background:linear-gradient(135deg,#95c33a,#a1cd39 50%,#8bbb34)}
.quote-card{position:absolute;top:81px;width:130px;height:120px;box-shadow:0 4px 6px rgba(0,0,0,.25)}
.quote-photo{height:80px}
.quote-person{height:40px;background:rgba(70,70,70,.92);display:flex;align-items:center;padding:0 8px;gap:8px}
.avatar{width:26px;height:26px;background:#9a9a9a}
.quote-person b{display:block;font-size:6.8px;color:var(--white)}
.quote-person small{display:block;font-size:4.8px;color:#ddd}
.dots{position:absolute;top:222px;left:349px;display:flex;gap:4px}
.dots i{width:6px;height:6px;border-radius:50%;background:var(--white)}
.dots i.on{background:#4a90c8;border:1.5px solid var(--white)}

/* news */
.news{position:absolute;left:0;top:868px;width:743px;height:184px;background:var(--white)}
.news-title{position:absolute;top:18px;width:100%;text-align:center;color:var(--ink);font-size:17px;font-weight:800;line-height:18px}
.news-sub{position:absolute;top:37px;width:100%;text-align:center;font-size:6.5px;color:#333}
.news-item{position:absolute;top:66px;width:130px}
.news-item h4{font-size:10.5px;font-weight:700;color:#222;line-height:12.5px}
.news-item p{margin-top:6px;font-size:5.2px;line-height:8px;color:#666}
.btn-green{position:absolute;top:83px;border:1px solid var(--green);color:var(--green);font-size:5.8px;font-weight:600;padding:2px 7px}

/* footer */
.site-footer{position:absolute;left:0;top:1052px;width:743px;height:148px;background:var(--footer);color:var(--white)}
.foot-h{position:absolute;top:22px;font-size:6.5px;font-weight:700}
.foot-brand{position:absolute;left:166px;top:47px;display:flex;align-items:center;gap:5px}
.foot-brand .brand-dot{width:17px;height:17px;background:var(--white)}
.foot-brand span{font-size:10.5px;font-weight:700}
.foot-text{position:absolute;left:166px;top:73px;width:135px;font-size:5.2px;line-height:8px;color:#ddd}
.links{position:absolute;left:337px;top:44px;font-size:5.2px;line-height:14px;color:#ddd;list-style:none}
.links li::before{content:"• ";color:var(--green)}
.contact{position:absolute;left:447px;top:44px;font-size:5.2px;line-height:10px}
.contact em{font-style:normal;color:var(--green)}
.newsletter{position:absolute;left:447px;top:88px;width:129px;height:12px;border:1px solid var(--green);display:flex;font-size:5.2px}
.newsletter span{flex:1;padding:2px 4px}
.newsletter b{width:38px;border-left:1px solid var(--green);color:var(--green);text-align:center;padding-top:2px}
.foot-rule{position:absolute;left:166px;top:116px;width:410px;height:1px;background:#3a3a3a}
.copyright{position:absolute;left:166px;top:127px;font-size:5.2px}
.copyright em{font-style:normal;color:var(--green)}
</style>
</head>
<body>

<header class="site-header">
  <div class="brand"><span class="brand-dot"></span><span class="brand-name">Freightmere Alliance</span></div>
  <nav class="main-nav"><span>Our Company</span><span>Our Expretise</span><span>Our Network</span><span>Investor Relations</span></nav>
  <div class="round-btn" style="left:536px"><svg width="7" height="7" viewBox="0 0 10 10"><circle cx="4" cy="4" r="3" fill="none" stroke="#a1cd39" stroke-width="1.4"/><line x1="6.3" y1="6.3" x2="9" y2="9" stroke="#a1cd39" stroke-width="1.4"/></svg></div>
  <div class="round-btn" style="left:560px"><svg width="8" height="6" viewBox="0 0 8 6"><rect width="8" height="6" fill="#c33"/><rect y="1.5" width="8" height="1" fill="#fff"/><rect y="3.5" width="8" height="1" fill="#fff"/><rect width="3.5" height="3" fill="#2b4a8f"/></svg></div>
</header>

<section class="hero" role="img" aria-label="Cargo aircraft being loaded with palletised freight under a blue sky">
  <div class="hero-kicker">BUSINESS TO FREIGHTMERE ALLIANCE GROUP</div>
  <h1 class="hero-title">PROVIDING FIRST CLASS<br>FREIGHT SERVICES</h1>
  <article class="service-card" style="left:166px">
    <h3>Air Freight</h3>
    <p>Lorem Ipsum has been the industry's standard dummy text ever since the 1500s, when an unknown printer took a galley of type and scrambled it to make a type specimen book.</p>
    <span class="btn-outline">Read More</span>
  </article>
  <article class="service-card" style="left:307px">
    <h3>Ocean Freight</h3>
    <p>Lorem Ipsum has been the industry's standard dummy text ever since the 1500s, when an unknown printer took a galley of type and scrambled it to make a type specimen book.</p>
    <span class="btn-outline">Read More</span>
  </article>
  <article class="service-card" style="left:447px">
    <h3>Warehousing<br>&amp; Distribution</h3>
    <p>Lorem Ipsum has been the industry's standard dummy text ever since the 1500s, when an unknown printer took a galley of type and scrambled it to make</p>
    <span class="btn-outline">Read More</span>
  </article>
</section>

<section class="industries">
  <div class="map-fill" role="img" aria-label="Faint dotted world map"></div>
  <h2 class="section-title" style="top:35px">OUR INDUSTRY SOLUTIONS COVER</h2>
  <svg class="title-rule" style="top:55px" viewBox="0 0 111 6"><path d="M0 1 L48 1 L55.5 5 L63 1 L111 1" fill="none" stroke="#a1cd39" stroke-width="1"/></svg>

  <div class="industry" style="left:168px;top:92px"><div class="head"><svg class="icon" viewBox="0 0 13 11"><path d="M3 2 Q6.5 9 10 2 M6.5 6 V11" fill="none" stroke="#a1cd39" stroke-width="1.2"/></svg>Flowers</div><p>Lorem Ipsum is simply dummy text of the printing and typesetting industry.</p></div>
  <div class="industry" style="left:273px;top:92px"><div class="head"><svg class="icon" viewBox="0 0 13 11"><path d="M1 10 L10 1 M4 10 L12 3" fill="none" stroke="#a1cd39" stroke-width="1.2"/></svg>FMCG including,<br>fruits, vegetables</div><p style="margin-top:2px">Lorem Ipsum is simply dummy text of the printing and typesetting industry.</p></div>
  <div class="industry" style="left:378px;top:92px"><div class="head"><svg class="icon" viewBox="0 0 13 11"><circle cx="6.5" cy="7" r="3" fill="none" stroke="#a1cd39" stroke-width="1.2"/><circle cx="2.5" cy="3" r="1.3" fill="#a1cd39"/><circle cx="10.5" cy="3" r="1.3" fill="#a1cd39"/></svg>Live Animals</div><p>Lorem Ipsum is simply dummy text of the printing and typesetting industry.</p></div>
  <div class="industry" style="left:483px;top:92px"><div class="head"><svg class="icon" viewBox="0 0 13 11"><path d="M1 8 V5 L3 2 H10 L12 5 V8 Z" fill="#a1cd39"/></svg>Automotive</div><p>Lorem Ipsum is simply dummy text of the printing and typesetting industry.</p></div>

  <div class="industry" style="left:168px;top:159px"><div class="head"><svg class="icon" viewBox="0 0 13 11"><path d="M0 1 H2 L4 7 H11 L12 3 H3" fill="none" stroke="#a1cd39" stroke-width="1.2"/><circle cx="5" cy="9.5" r="1" fill="#a1cd39"/><circle cx="10" cy="9.5" r="1" fill="#a1cd39"/></svg>Consumer Goods</div><p>Lorem Ipsum is simply dummy text of the printing and typesetting industry.</p></div>
  <div class="industry" style="left:273px;top:159px"><div class="head"><svg class="icon" viewBox="0 0 13 11"><path d="M1 10 V3 L4 5 V3 L7 5 V3 L10 5 V1 H12 V10 Z" fill="none" stroke="#a1cd39" stroke-width="1.2"/></svg>Industrial</div><p>Lorem Ipsum is simply dummy text of the printing and typesetting industry.</p></div>
  <div class="industry" style="left:378px;top:159px"><div class="head"><svg class="icon" viewBox="0 0 13 11"><path d="M6.5 1 V10 M3 10 H10 M6.5 3 H11" fill="none" stroke="#a1cd39" stroke-width="1.4"/></svg>Oil &amp; Gas</div><p>Lorem Ipsum is simply dummy text of the printing and typesetting industry.</p></div>
  <div class="industry" style="left:483px;top:159px"><div class="head"><svg class="icon" viewBox="0 0 13 11"><rect x="3" y="1" width="5" height="10" rx="2.5" transform="rotate(40 6.5 6)" fill="none" stroke="#a1cd39" stroke-width="1.3"/></svg>Pharma</div><p>Lorem Ipsum is simply dummy text of the printing and typesetting industry.</p></div>

  <div class="industry" style="left:168px;top:230px"><div class="head"><svg class="icon" viewBox="0 0 13 11"><rect x="1" y="1" width="9" height="9" fill="none" stroke="#a1cd39" stroke-width="1.2"/><path d="M3 4 H8 M3 6.5 H7" stroke="#a1cd39"/></svg>Event Logistics</div><p>Lorem Ipsum is simply dummy text of the printing and typesetting industry.</p></div>
  <div class="industry" style="left:273px;top:230px"><div class="head"><svg class="icon" viewBox="0 0 13 11"><path d="M2 10 H11 L9 4 H4 Z M6.5 4 V1" fill="none" stroke="#a1cd39" stroke-width="1.2"/></svg>Project Logistics</div><p>Lorem Ipsum is simply dummy text of the printing and typesetting industry.</p></div>
</section>

<section class="testimonials">
  <h2 class="section-title" style="top:36px">WHAT CUSTOMERS ARE SAYING ABOUT US</h2>
  <svg class="title-rule" style="top:56px" viewBox="0 0 111 6"><path d="M0 1 L48 1 L55.5 5 L63 1 L111 1" fill="none" stroke="#ffffff" stroke-width="1"/></svg>

  <article class="quote-card" style="left:166px">
    <div class="quote-photo" role="img" aria-label="Pink tulips beside a wrapped gift box" style="background:linear-gradient(135deg,#f2d4ea,#d986c4)"></div>
    <div class="quote-person"><div class="avatar" role="img" aria-label="Customer portrait"></div><div><b>Dana Marie Holt</b><small>CEO, Bright Orchard Inc.</small></div></div>
  </article>
  <article class="quote-card" style="left:307px">
    <div class="quote-photo" role="img" aria-label="Blue and white medicine capsules" style="background:linear-gradient(135deg,#dfe6f2,#3857a8)"></div>
    <div class="quote-person"><div class="avatar" role="img" aria-label="Customer portrait"></div><div><b>Dana Marie Holt</b><small>CEO, Bright Orchard Inc.</small></div></div>
  </article>
  <article class="quote-card" style="left:447px">
    <div class="quote-photo" role="img" aria-label="Assorted fresh exotic fruits" style="background:linear-gradient(135deg,#c23a2a,#6a8a2a 60%,#e2a530)"></div>
    <div class="quote-person"><div class="avatar" role="img" aria-label="Customer portrait"></div><div><b>Dana Marie Holt</b><small>CEO, Bright Orchard Inc.</small></div></div>
  </article>
  <div class="dots"><i></i><i class="on"></i><i></i><i></i><i></i></div>
</section>

<section class="news">
  <h2 class="news-title">NEWS</h2>
  <div class="news-sub">STAY TUNED</div>
  <article class="news-item" style="left:166px"><h4>WHAT CUSTOMERS TIME SENSITIVE</h4><p>Lorem Ipsum has been the industry's standard dummy text ever since the 1500s, when an unknown printer took a galley of type and scrambled it to make a type specimen book.</p><span class="btn-green">Read More</span></article>
  <article class="news-item" style="left:307px"><h4>WHAT CUSTOMERS TIME SENSITIVE</h4><p>Lorem Ipsum has been the industry's standard dummy text ever since the 1500s, when an unknown printer took a galley of type and scrambled it to make a type specimen book.</p><span class="btn-green">Read More</span></article>
  <article class="news-item" style="left:447px"><h4>AND CONFIDENCEARE SAYING ABOUT US</h4><p>Lorem Ipsum has been the industry's standard dummy text ever since the 1500s, when an unknown printer took a galley of type and scrambled it to make a type specimen book.</p><span class="btn-green">Read More</span></article>
</section>

<footer class="site-footer">
  <div class="foot-h" style="left:166px">ABOUT OUR COMPANY</div>
  <div class="foot-h" style="left:337px">USEFUL LINKS</div>
  <div class="foot-h" style="left:447px">CONTACT INFO</div>
  <div class="foot-brand"><span class="brand-dot"></span><span>Freightmere Alliance</span></div>
  <p class="foot-text">dummy text ever since the 1500s, when an unknown printer took a galley of type and scrambled it to make a type specimen book.</p>
  <ul class="links"><li>Our Company</li><li>Our Expretise</li><li>Our Network</li><li>Investor Relations</li></ul>
  <div class="contact"><em>Address :</em> Harbourline Cargo, 12 Quayside Row, Portmere<br><em>Phone Number :</em> +00 20 5550 1420</div>
  <div class="foot-h" style="left:447px;top:76px">NEWSLETTER</div>
  <div class="newsletter"><span>Address Email</span><b>Subscribe</b></div>
  <div class="foot-rule"></div>
  <div class="copyright"><em>2015 Freightmere Alliance</em>- All Rights Reserved</div>
</footer>

</body>
</html>
```